Business Card Project

We are a small consulting firm. You can experiment with any design.
Must have:
1) Company name - OLUNDEX International
2) Company slogan - simple solutions for complex problems
3) Name/Title/Phone/Email/WWW/ - use anything you like as an example.

Industry/Entity Type

Business

```html
<!DOCTYPE html>
<html lang="en">
<head>
<meta charset="utf-8">
<title>OLUNDEX International – Business Card</title>
<link rel="stylesheet" href="https://fonts.googleapis.com/css2?family=Source+Sans+3:wght@400;600&display=swap">
<style>
  :root {
    --page-bg: #eef1f5;
    --band-deep: #1b2580;
    --band-mid: #2f43b5;
    --band-light: #4a63d1;
    --card-top: #ffffff;
    --card-bottom: #d9f1f8;
    --name-blue: #2e4bb8;
    --text-grey: #6b7480;
    --logo-white: #ffffff;
    --slogan-white: rgba(255, 255, 255, 0.85);
  }
  * { margin: 0; padding: 0; box-sizing: border-box; }
  html, body {
    width: 1200px;
    height: 751px;
    overflow: hidden;
  }
  body {
    background: var(--page-bg);
    font-family: "Source Sans 3", "Myriad Pro", Arial, sans-serif;
    display: flex;
    align-items: center;
    justify-content: center;
  }
  .business-card {
    position: relative;
    width: 700px;
    height: 400px;
    border-radius: 26px;
    overflow: hidden;
    background: linear-gradient(180deg, var(--card-top) 40%, var(--card-bottom) 100%);
    box-shadow: 0 10px 30px rgba(20, 30, 60, 0.18);
  }
  .header-band {
    position: absolute;
    top: 0;
    left: 0;
    width: 700px;
    height: 200px;
  }
  .brand {
    position: absolute;
    top: 46px;
    left: 0;
    width: 100%;
    display: flex;
    align-items: center;
    justify-content: center;
    gap: 16px;
  }
  .brand-dot {
    flex: 0 0 auto;
    width: 46px;
    height: 46px;
    border-radius: 50%;
    background: var(--logo-white);
  }
  .brand-name {
    color: var(--logo-white);
    font-weight: 600;
    font-size: 36px;
    letter-spacing: 1px;
    line-height: 1;
    white-space: nowrap;
  }
  .slogan {
    position: absolute;
    top: 106px;
    left: 0;
    width: 100%;
    text-align: center;
    color: var(--slogan-white);
    font-size: 15px;
    letter-spacing: 2px;
    text-transform: uppercase;
    white-space: nowrap;
  }
  .person {
    position: absolute;
    top: 218px;
    left: 0;
    width: 100%;
    text-align: center;
  }
  .person-name {
    color: var(--name-blue);
    font-weight: 400;
    font-size: 27px;
    line-height: 1.1;
  }
  .person-title {
    color: var(--text-grey);
    font-size: 15px;
    margin-top: 4px;
  }
  .contact {
    position: absolute;
    top: 318px;
    left: 0;
    width: 100%;
    text-align: center;
    color: var(--text-grey);
    font-size: 16px;
    line-height: 1.45;
  }
  .contact .sep { margin: 0 6px; }
</style>
</head>
<body>
  <article class="business-card">
    <svg class="header-band" viewBox="0 0 700 200" aria-hidden="true">
      <defs>
        <linearGradient id="bandGradient" x1="0" y1="0" x2="1" y2="1">
          <stop offset="0" stop-color="#1b2580"/>
          <stop offset="0.6" stop-color="#2f43b5"/>
          <stop offset="1" stop-color="#4a63d1"/>
        </linearGradient>
      </defs>
      <path fill="url(#bandGradient)" d="M0,0 H700 V150
        C690,158 680,140 668,150 C655,162 648,146 636,152 C622,160 612,170 600,156
        C590,146 580,160 566,154 C550,148 540,166 526,158 C512,150 500,146 488,156
        C476,166 462,150 450,154 C436,158 430,170 414,162 C400,156 392,148 378,156
        C364,164 352,152 340,158 C326,164 316,172 300,160 C288,152 278,150 264,158
        C250,166 240,154 228,160 C214,166 204,174 190,164 C178,156 166,160 152,168
        C138,176 128,164 116,170 C102,178 90,186 76,176 C64,168 52,172 38,180
        C24,188 14,178 0,186 Z"/>
    </svg>

    <div class="brand">
      <span class="brand-dot"></span>
      <span class="brand-name">OLUNDEX International</span>
    </div>
    <p class="slogan">simple solutions for complex problems</p>

    <div class="person">
      <p class="person-name">Daren Kolby</p>
      <p class="person-title">Sales Manager</p>
    </div>

    <div class="contact">
      <p>Harbor Lane<span class="sep">|</span>ph: 41592 604 31<span class="sep">|</span>mob: 061 52740 3916</p>
      <p>email: daren@olundexco.com<span class="sep">|</span>www.olundexcorp.com</p>
    </div>
  </article>
</body>
</html>
```